Vintage soap dispenser label

I'm making a series of glass bottle soap dispensers (soap, lotion, shampoo, etc.). I really love a competitor's design, but I don't want to copy it. I'm interested in the clean, urban vintage style. There can be a lot of filler text as in their design which fills the negative space, but note that the buyer will fill the bottles with their own products, so things like "100% Natural Ingredients" and the like are somewhat bogus. Because they are to be refillable, reusable bottles, some text to that effect may be more appropriate, plus our company name "Velmora Home", and perhaps the style of the bottle "Boston Round" and other text like the size of the bottle. I need a basic design, 3.25" wide x 3.5" tall and I will adjust the text as necessary for the various products my buyers will use. My competitor that is very similar to my business is https://qorvu.ly/8LmZr5k. As you can see, they have a signature style. I'd like my own signature style. (I plan to have a vintage line and a contemporary line of products, so I'll likely be posting a second request for that.)

Requirements
Should not have
• Not too ornate. Should be somewhat minimalistic

```html
<!DOCTYPE html>
<html lang="en">
<head>
<meta charset="utf-8">
<title>Velmora Home – Hand Soap Label</title>
<link rel="stylesheet" href="https://fonts.googleapis.com/css2?family=Oswald:wght@700&family=Barlow+Semi+Condensed:wght@600;700&display=swap">
<style>
  :root {
    --ink: #141414;
    --paper: #ffffff;
  }
  html, body {
    margin: 0;
    padding: 0;
    width: 1113px;
    height: 1200px;
    overflow: hidden;
    background: var(--paper);
  }
  .label {
    display: block;
    width: 1113px;
    height: 1200px;
  }
  .frame, .rule, .banner, .banner-inner, .size-box {
    fill: none;
    stroke: var(--ink);
  }
  .banner { fill: var(--paper); }
  .ornament-mark { fill: var(--ink); }
  .brand-name, .brand-sub {
    font-family: "Barlow Semi Condensed", "Arial Narrow", sans-serif;
    font-weight: 700;
    fill: var(--ink);
    text-anchor: middle;
  }
  .brand-name { font-size: 78px; letter-spacing: 3px; }
  .brand-sub { font-size: 34px; letter-spacing: 4px; }
  .product-name {
    font-family: "Oswald", "Arial Narrow", sans-serif;
    font-weight: 700;
    font-size: 190px;
    fill: var(--ink);
    text-anchor: middle;
  }
  .tagline, .size-text {
    font-family: "Barlow Semi Condensed", "Arial Narrow", sans-serif;
    font-weight: 700;
    fill: var(--ink);
    text-anchor: middle;
  }
  .tagline { font-size: 44px; letter-spacing: 3px; }
  .size-text { font-size: 38px; letter-spacing: 1px; }
</style>
</head>
<body>
<svg class="label" viewBox="0 0 1113 1200" xmlns="http://www.w3.org/2000/svg">
  <!-- outer frame -->
  <rect class="frame" x="40" y="40" width="1033" height="1126" stroke-width="9"/>

  <!-- diagonal rules into banner -->
  <line class="rule" x1="40" y1="186" x2="366" y2="291" stroke-width="5"/>
  <line class="rule" x1="1073" y1="186" x2="750" y2="291" stroke-width="5"/>

  <!-- banner -->
  <polygon class="banner" points="366,40 750,40 750,324 558,405 366,324" stroke-width="8"/>
  <polyline class="banner-inner" points="366,300 558,381 750,300" stroke-width="5"/>

  <!-- brand -->
  <text class="brand-name" x="558" y="250">VELMORA</text>
  <text class="brand-sub" x="558" y="304">HOME</text>

  <!-- product -->
  <text class="product-name" x="556" y="678" textLength="850" lengthAdjust="spacingAndGlyphs">HAND SOAP</text>

  <!-- tagline rules -->
  <g class="tagline-rules">
    <line class="rule" x1="306" y1="756" x2="810" y2="756" stroke-width="4"/>
    <polygon class="ornament-mark" points="300,756 310,749 320,756 310,763"/>
    <polygon class="ornament-mark" points="796,756 806,749 816,756 806,763"/>
    <polygon class="ornament-mark" points="548,756 558,750 568,756 558,762"/>
    <line class="rule" x1="306" y1="846" x2="810" y2="846" stroke-width="4"/>
    <polygon class="ornament-mark" points="300,846 310,839 320,846 310,853"/>
    <polygon class="ornament-mark" points="796,846 806,839 816,846 806,853"/>
    <polygon class="ornament-mark" points="548,846 558,840 568,846 558,852"/>
  </g>
  <text class="tagline" x="558" y="817">★ REFILL – REUSE ★</text>

  <!-- size strip -->
  <line class="rule" x1="40" y1="1056" x2="1073" y2="1056" stroke-width="5"/>
  <rect class="size-box" x="321" y="1023" width="483" height="66" fill="#fff" stroke-width="6" style="fill: var(--paper);"/>
  <line class="rule" x1="561" y1="1023" x2="561" y2="1089" stroke-width="6"/>
  <text class="size-text" x="441" y="1070">500ML</text>
  <text class="size-text" x="682" y="1070">16 FL OZ</text>
</svg>
</body>
</html>
```